Business Card Design Project

I need a new business card design for my building/development company: Kestrel Ridge Builders.

We specialise in small sub-divisions, multi-story developments and new house builds.
We handle the whole process from concept stage right throught to a fully developed property.
Updates

Target Market(s)

people looking to develop their property and need help. New property buyers

Industry/Entity Type

House

Requirements
Must have
• My logo on both sides:
Side 1: Logo taking up whole side as per old card but with a color/style change.

Side 2: Contact page: include logo but the rest just surprise me!

All contact details will be: (and need to be changable for each employee) I'll inform you of specifics before printing.

Name Surname
Position ie. Managing director
M: insert mobile
E: insert email
P.O. Box 518, Ashwell, Vic, 3094
www.kestrelridgebuilders.com.au

Nice to have
• Colors i'd like: (not necessarily all but this is the basic idea)

Black, blue, grey, silver, white

```html
<!DOCTYPE html>
<html lang="en">
<head>
<meta charset="utf-8">
<title>Kestrel Ridge Builders – Business Card</title>
<link rel="stylesheet" href="https://fonts.googleapis.com/css2?family=Arimo:wght@400;700&family=Open+Sans:wght@600&display=swap">
<style>
  :root {
    --page-bg: #e8e5e0;
    --card-black: #050505;
    --accent-grey: #2b2b2e;
    --brand-blue: #1a8fd6;
    --stripe-blue: #0e95db;
    --panel-silver: #d9dadc;
    --text-white: #ffffff;
    --text-soft: #f0f0f0;
  }
  * { box-sizing: border-box; margin: 0; padding: 0; }
  html, body {
    width: 943px; height: 1200px; overflow: hidden;
    background: var(--page-bg);
    font-family: "Arimo", Arial, sans-serif;
  }
  .canvas { position: relative; width: 943px; height: 1200px; }

  .card {
    position: absolute; left: 87px; width: 769px; height: 472px;
    background: var(--card-black); overflow: hidden;
  }
  .card--front { top: 112px; }
  .card--back { top: 636px; }

  /* front */
  .front-pattern { position: absolute; inset: 0; width: 100%; height: 100%; }
  .brand-mark {
    position: absolute; left: 313px; top: 100px; width: 144px; height: 144px;
    background: var(--brand-blue);
  }
  .brand-lockup {
    position: absolute; left: 0; right: 0; top: 276px; text-align: center;
  }
  .brand-name {
    font-weight: 700; font-size: 50px; letter-spacing: -0.5px;
    color: var(--text-white); line-height: 1; white-space: nowrap;
  }
  .brand-tagline {
    margin-top: 8px;
    font-family: "Open Sans", Arial, sans-serif; font-weight: 600;
    font-size: 22px; color: var(--text-white); letter-spacing: 0.2px;
  }

  /* back */
  .back-accent { position: absolute; left: 390px; top: 0; width: 379px; height: 258px; }
  .back-mark {
    position: absolute; left: 590px; top: 40px; width: 74px; height: 74px;
    background: var(--brand-blue);
  }
  .back-brand {
    position: absolute; right: 22px; top: 140px; white-space: nowrap;
    font-weight: 700; font-size: 26px; color: var(--text-white); letter-spacing: -0.3px;
  }
  .staff { position: absolute; left: 83px; top: 143px; }
  .staff-name { font-weight: 700; font-size: 23px; color: var(--brand-blue); }
  .staff-role { margin-top: 8px; font-size: 20px; color: var(--text-white); }

  .contact-panel {
    position: absolute; left: 0; top: 262px; width: 464px; height: 113px;
    background: var(--panel-silver); border-radius: 0 8px 8px 0;
    padding: 8px 0 0 83px;
    font-size: 21px; line-height: 30px; color: var(--brand-blue);
    white-space: nowrap;
  }
  .contact-label { font-weight: 700; }

  .website {
    position: absolute; left: 0; right: 0; top: 412px; text-align: center;
    font-size: 27px; color: var(--text-soft);
  }
  .base-stripe {
    position: absolute; left: 0; right: 0; bottom: 0; height: 14px;
    background: var(--stripe-blue);
  }
</style>
</head>
<body>
<main class="canvas">

  <section class="card card--front" aria-label="Card front">
    <svg class="front-pattern" viewBox="0 0 769 472" role="img" aria-label="Repeating faint brand pattern across the dark background">
      <defs>
        <linearGradient id="patternTone" x1="0" y1="0" x2="0" y2="1">
          <stop offset="0" stop-color="#141416"/>
          <stop offset="0.5" stop-color="#1d1d1f"/>
          <stop offset="1" stop-color="#121214"/>
        </linearGradient>
      </defs>
      <rect width="769" height="472" fill="url(#patternTone)"/>
    </svg>
    <div class="brand-mark" aria-hidden="true"></div>
    <div class="brand-lockup">
      <p class="brand-name">Kestrel Ridge Builders</p>
      <p class="brand-tagline">renovation-construction-development</p>
    </div>
  </section>

  <section class="card card--back" aria-label="Card back">
    <svg class="back-accent" viewBox="0 0 379 258" role="img" aria-label="Large faint brand decoration behind the name">
      <defs>
        <radialGradient id="accentTone" cx="0.6" cy="0.4" r="0.7">
          <stop offset="0" stop-color="#2e2e31"/>
          <stop offset="1" stop-color="#050505"/>
        </radialGradient>
      </defs>
      <rect width="379" height="258" fill="url(#accentTone)"/>
    </svg>
    <div class="back-mark" aria-hidden="true"></div>
    <p class="back-brand">Kestrel Ridge Builders</p>

    <div class="staff">
      <p class="staff-name">Marcus Hale</p>
      <p class="staff-role">Director</p>
    </div>

    <div class="contact-panel">
      <p><span class="contact-label">M</span>: 0400 555 218</p>
      <p><span class="contact-label">E</span>: marcus@kestrelridgebuilders.com.au</p>
      <p>P.O. Box 518, Ashwell, Vic, 3094</p>
    </div>

    <p class="website">www.kestrelridgebuilders.com.au</p>
    <div class="base-stripe"></div>
  </section>

</main>
</body>
</html>
```